Business Card Design Project

I am community manager and social media strategist. I need a double sided business card with company logo and name. Looking for something professional, elegant but also a little bit original.

• - The logo and the colours are the company colours and a required to stay.
- The size should be: 84 x 55 mm (or 3.30 x 2.16)
- The file size should be: 1039 x 697 pixels (300 dpi)
- I'd like rounded corners. :)

Use the following contact information for the card:

Léonie Vardin
Stratégie médias sociaux / community management / édition de sites sociaux
mob. : 0687529103
leonie.vardin@postelune.fr
Twitter. : @lvardin
Skype : vardin.leonie

```html
<!DOCTYPE html>
<html lang="fr">
<head>
<meta charset="utf-8">
<title>Léonie Vardin — Carte de visite</title>
<link rel="stylesheet" href="https://fonts.googleapis.com/css2?family=Open+Sans:wght@300;400;600;700&display=swap">
<style>
  :root {
    --page-bg: #d9d9d9;
    --blue-deep: #0d3f73;
    --blue-mid: #1565a8;
    --blue-glow: #3f86c6;
    --band-dark: #1d1e20;
    --band-darker: #151617;
    --bevel-light: #6a6d72;
    --bevel-dark: #0a0a0b;
    --text-white: #ffffff;
    --text-soft: #d5e3f1;
    --text-grey: #9a9ca0;
    --icon-grey: #5b5d61;
  }
  * { box-sizing: border-box; margin: 0; padding: 0; }
  html, body { width: 1200px; height: 900px; overflow: hidden; }
  body {
    background: var(--page-bg);
    font-family: "Open Sans", Arial, sans-serif;
    display: flex;
    align-items: center;
    justify-content: center;
    gap: 60px;
  }
  .card {
    position: relative;
    width: 520px;
    height: 340px;
    border-radius: 14px;
    overflow: hidden;
    box-shadow: 0 12px 30px rgba(0,0,0,0.25);
    background: var(--band-dark);
  }
  .card__face {
    position: absolute;
    left: 0; top: 0; right: 0;
    background:
      radial-gradient(ellipse 55% 70% at 45% 35%, var(--blue-glow) 0%, rgba(63,134,198,0) 70%),
      linear-gradient(180deg, var(--blue-mid) 0%, var(--blue-deep) 100%);
  }
  .card__band {
    position: absolute;
    left: 0; right: 0; bottom: 0;
    background: linear-gradient(180deg, var(--band-dark) 0%, var(--band-darker) 100%);
    border-top: 2px solid var(--bevel-light);
    box-shadow: 0 -3px 0 var(--bevel-dark) inset, 0 -1px 4px rgba(0,0,0,0.5);
  }

  /* Back side */
  .card--back .card__face { height: 215px; }
  .card--back .card__band { top: 215px; }
  .brand {
    position: absolute;
    left: 0; right: 0; top: 80px;
    display: flex;
    align-items: center;
    justify-content: center;
    gap: 12px;
  }
  .brand__mark {
    width: 22px; height: 22px;
    border-radius: 50%;
    background: var(--text-white);
  }
  .brand__name {
    color: var(--text-white);
    font-weight: 700;
    font-size: 30px;
    letter-spacing: 3px;
  }
  .back-tagline {
    position: absolute;
    left: 0; right: 0; top: 56px;
    text-align: center;
    color: var(--text-grey);
    font-size: 11.5px;
    letter-spacing: 0.3px;
  }

  /* Front side */
  .card--front .card__face { height: 232px; }
  .card--front .card__band { top: 232px; }
  .identity {
    position: absolute;
    right: 44px; top: 72px;
    text-align: right;
  }
  .identity__name {
    color: var(--text-white);
    font-weight: 300;
    font-size: 44px;
    line-height: 1;
    letter-spacing: -0.5px;
    text-shadow: 0 1px 2px rgba(0,0,0,0.35);
  }
  .identity__roles {
    margin-top: 12px;
    color: var(--text-soft);
    font-size: 13px;
    line-height: 1.25;
  }
  .contacts {
    position: absolute;
    left: 38px; right: 30px; top: 26px;
    display: grid;
    grid-template-columns: 1fr 1.35fr;
    row-gap: 18px;
    column-gap: 16px;
  }
  .contact {
    display: flex;
    align-items: center;
    gap: 8px;
    color: var(--text-grey);
    font-size: 12.5px;
    white-space: nowrap;
  }
  .contact__icon {
    flex: none;
    width: 20px; height: 20px;
    border-radius: 50%;
    background: var(--icon-grey);
    display: flex;
    align-items: center;
    justify-content: center;
  }
  .contact__icon svg { width: 12px; height: 12px; }
</style>
</head>
<body>

  <section class="card card--back" aria-label="Recto">
    <div class="card__face">
      <div class="brand">
        <span class="brand__mark"></span>
        <span class="brand__name">NORVELA</span>
      </div>
    </div>
    <div class="card__band">
      <p class="back-tagline">Stratégie médias sociaux / community management / édition de sites sociaux</p>
    </div>
  </section>

  <section class="card card--front" aria-label="Verso">
    <div class="card__face">
      <div class="identity">
        <h1 class="identity__name">Léonie Vardin</h1>
        <p class="identity__roles">Stratégie médias sociaux<br>community management<br>édition de sites sociaux</p>
      </div>
    </div>
    <div class="card__band">
      <ul class="contacts" style="list-style:none">
        <li class="contact">
          <span class="contact__icon">
            <svg viewBox="0 0 12 12" aria-hidden="true"><rect x="3.5" y="1" width="5" height="10" rx="1" fill="none" stroke="#c9cbce" stroke-width="1.2"/><circle cx="6" cy="9.2" r="0.7" fill="#c9cbce"/></svg>
          </span>
          : 0687529103
        </li>
        <li class="contact">
          <span class="contact__icon"></span>
          : leonie.vardin@postelune.fr
        </li>
        <li class="contact">
          <span class="contact__icon"></span>
          : @lvardin
        </li>
        <li class="contact">
          <span class="contact__icon"></span>
          : vardin.leonie
        </li>
      </ul>
    </div>
  </section>

</body>
</html>
```